Road Construction Company needs business cards

We would like a new business card designed for our business.

We're a road construction company based in Qld, Australia.

Can the business card please have the following information on it.

Name: Brent Malvoy
Position: General Manager
Phone: 0471 592 304
Email: Brent.malvoy@quendix.com.au
Address: 87 Harrowgate Ave, Pindarra, QLD, 4000
Website: www.quendix.com.au

Visually we'd like the card to be professional and simple.

Attached is our logo.

Our website is www.quendix.com.au

Target Market(s)

Men aged 25-60

Contact Information for Business Card

As listed in project description

Font styles to use
Serif

Requirements
Must have
• Large logo on back of card

```html
<!DOCTYPE html>
<html lang="en">
<head>
<meta charset="utf-8">
<title>Quendix Business Card</title>
<link href="https://fonts.googleapis.com/css2?family=Exo+2:wght@400;500&family=Michroma&display=swap" rel="stylesheet">
<style>
  :root {
    --backdrop: #201d1b;
    --card: #1b1b1c;
    --blue-deep: #0b57ad;
    --blue-light: #2a9ad6;
    --text: #f2f2f2;
  }
  * { margin: 0; padding: 0; box-sizing: border-box; }
  html, body { width: 1200px; height: 842px; overflow: hidden; background: var(--backdrop); }
  .canvas {
    position: relative; width: 1200px; height: 842px;
    display: flex; align-items: center; justify-content: center; gap: 60px;
  }
  .card {
    position: relative; width: 520px; height: 298px;
    background: var(--card); overflow: hidden;
    box-shadow: 0 12px 30px rgba(0,0,0,0.5);
  }
  /* Front */
  .band { position: absolute; left: 0; right: 0; height: 16px; background: var(--blue-deep); }
  .band--top { top: 0; }
  .band--bottom { bottom: 0; }
  .details {
    position: absolute; inset: 16px 0; display: flex; flex-direction: column;
    align-items: center; justify-content: center; text-align: center;
    font-family: "Exo 2", sans-serif; color: var(--text); font-size: 16px; line-height: 1.25;
  }
  .details__name {
    font-family: "Michroma", sans-serif; color: var(--blue-light);
    font-size: 17px; letter-spacing: 1px; text-transform: uppercase; line-height: 1.1;
  }
  .details__role { font-size: 16px; }
  .divider { width: 64px; height: 2px; background: var(--blue-light); margin: 10px 0 12px; }
  .details__accent { color: var(--blue-light); }
  .details__address { margin-top: 2px; }
  /* Back */
  .side-mark { position: absolute; width: 40px; height: 86px; }
  .side-mark__block { position: absolute; top: 0; width: 34px; height: 100%; background: var(--blue-deep); }
  .side-mark__line { position: absolute; top: 0; width: 4px; height: 100%; background: var(--blue-light); }
  .side-mark--left { left: 0; top: 150px; }
  .side-mark--left .side-mark__block { left: 0; }
  .side-mark--left .side-mark__line { left: 38px; }
  .side-mark--right { right: 0; top: 62px; }
  .side-mark--right .side-mark__block { right: 0; }
  .side-mark--right .side-mark__line { right: 38px; }
  .brand {
    position: absolute; inset: 0; display: flex; align-items: center; justify-content: center;
    font-family: "Michroma", sans-serif; font-size: 40px; letter-spacing: 3px;
    color: var(--blue-deep); text-transform: uppercase;
  }
</style>
</head>
<body>
<main class="canvas">
  <section class="card card--front">
    <div class="band band--top"></div>
    <div class="details">
      <p class="details__name">Brent Malvoy</p>
      <p class="details__role">General Manager</p>
      <div class="divider"></div>
      <p>0471 592 304</p>
      <p>Brent.malvoy@quendix.com.au</p>
      <p>www.<span class="details__accent">quendix.</span>com.au</p>
      <div class="divider"></div>
      <p class="details__address">87 Harrowgate Ave</p>
      <p>Pindarra, QLD, 4000</p>
    </div>
    <div class="band band--bottom"></div>
  </section>

  <section class="card card--back">
    <div class="side-mark side-mark--right"><span class="side-mark__block"></span><span class="side-mark__line"></span></div>
    <p class="brand">Quendix</p>
    <div class="side-mark side-mark--left"><span class="side-mark__block"></span><span class="side-mark__line"></span></div>
  </section>
</main>
</body>
</html>
```